VARQO Business card

Black card, double sided with company colors black, blue and white with slogan on back Your VARQO......

Industry/Entity Type

Business

```html
<!DOCTYPE html>
<html lang="en">
<head>
<meta charset="utf-8">
<title>VARQO Business Card</title>
<link rel="stylesheet" href="https://fonts.googleapis.com/css2?family=Quicksand:wght@300;400;500;600&display=swap">
<style>
  :root {
    --stage: #e6e6e6;
    --stage-edge: #cfcfcf;
    --card-black: #141213;
    --card-black-deep: #0b0a0a;
    --band-white: #ffffff;
    --brand-blue: #2a8fd6;
    --text-light: #e8e8e8;
    --text-muted: #9a9a9a;
    --icon-dark: #141213;
  }
  * { margin: 0; padding: 0; box-sizing: border-box; }
  html, body {
    width: 1200px;
    height: 800px;
    overflow: hidden;
  }
  body {
    background: radial-gradient(ellipse at 50% 40%, var(--stage) 55%, var(--stage-edge) 100%);
    font-family: "Quicksand", sans-serif;
    display: flex;
    align-items: center;
    justify-content: center;
    gap: 60px;
  }
  .card {
    width: 525px;
    height: 300px;
    border-radius: 30px;
    position: relative;
    overflow: hidden;
    box-shadow: 0 14px 30px rgba(0,0,0,0.22);
  }

  /* Front side */
  .card--front {
    background: linear-gradient(160deg, #1c1a1b 0%, var(--card-black) 45%, var(--card-black-deep) 100%);
  }
  .front__band {
    position: absolute;
    top: 0; left: 0; right: 0;
    height: 62px;
    background: var(--band-white);
    display: flex;
    align-items: center;
    padding-left: 34px;
  }
  .brand {
    display: flex;
    align-items: center;
    gap: 8px;
    font-weight: 600;
    letter-spacing: 1px;
  }
  .brand__dot {
    width: 12px; height: 12px;
    border-radius: 50%;
    background: var(--brand-blue);
  }
  .brand--small .brand__name { font-size: 17px; color: var(--icon-dark); }
  .contact-list {
    position: absolute;
    left: 34px;
    top: 100px;
    list-style: none;
    display: flex;
    flex-direction: column;
    gap: 9px;
  }
  .contact-list__item {
    display: flex;
    align-items: flex-start;
    gap: 10px;
    color: var(--text-light);
    font-size: 12px;
    line-height: 1.35;
  }
  .contact-list__icon {
    width: 14px; height: 14px;
    flex: none;
    margin-top: 1px;
  }
  .person {
    position: absolute;
    right: 44px;
    top: 128px;
    text-align: left;
    color: var(--text-light);
  }
  .person__name {
    font-weight: 300;
    font-size: 30px;
    letter-spacing: 0.5px;
    line-height: 1;
  }
  .person__role {
    font-size: 13px;
    font-weight: 400;
    margin-top: 4px;
    padding-left: 16px;
  }

  /* Back side */
  .card--back {
    background: linear-gradient(160deg, #222021 0%, var(--card-black) 55%, var(--card-black-deep) 100%);
    display: flex;
    flex-direction: column;
    align-items: center;
    justify-content: center;
  }
  .brand--large { flex-direction: row; }
  .brand--large .brand__dot { width: 22px; height: 22px; }
  .brand--large .brand__name { font-size: 40px; color: var(--band-white); }
  .back__slogan {
    margin-top: 8px;
    font-size: 11px;
    letter-spacing: 3px;
    color: var(--text-light);
    text-transform: uppercase;
  }
  .back__web {
    position: absolute;
    bottom: 18px;
    left: 0; right: 0;
    text-align: center;
    font-size: 9px;
    letter-spacing: 2px;
    color: var(--text-muted);
    text-transform: uppercase;
  }
</style>
</head>
<body>

  <section class="card card--front" aria-label="Business card front">
    <header class="front__band">
      <div class="brand brand--small">
        <span class="brand__dot"></span>
        <span class="brand__name">VARQO</span>
      </div>
    </header>

    <ul class="contact-list">
      <li class="contact-list__item">
        <svg class="contact-list__icon" viewBox="0 0 16 16" aria-hidden="true">
          <circle cx="8" cy="8" r="8" fill="#fff"/>
          <path d="M8 3.5a3 3 0 0 0-3 3c0 2.2 3 5.5 3 5.5s3-3.3 3-5.5a3 3 0 0 0-3-3z" fill="#141213"/>
          <circle cx="8" cy="6.5" r="1.1" fill="#fff"/>
        </svg>
        <span>#412, Linden Row<br>Calder Park</span>
      </li>
      <li class="contact-list__item">
        <svg class="contact-list__icon" viewBox="0 0 16 16" aria-hidden="true">
          <circle cx="8" cy="8" r="8" fill="#fff"/>
          <path d="M5.5 4h1.6l.8 2-1 .8a5.5 5.5 0 0 0 2.3 2.3l.8-1 2 .8v1.6c0 .5-.4.9-.9.9A7.1 7.1 0 0 1 4.6 4.9c0-.5.4-.9.9-.9z" fill="#141213"/>
        </svg>
        <span>0710 555 284</span>
      </li>
      <li class="contact-list__item">
        <svg class="contact-list__icon" viewBox="0 0 16 16" aria-hidden="true">
          <circle cx="8" cy="8" r="8" fill="#fff"/>
          <rect x="4" y="5" width="8" height="6" rx="0.8" fill="#141213"/>
          <path d="M4.3 5.4 8 8.3l3.7-2.9" stroke="#fff" stroke-width="0.9" fill="none"/>
        </svg>
        <span>hello@varqo.com</span>
      </li>
      <li class="contact-list__item">
        <svg class="contact-list__icon" viewBox="0 0 16 16" aria-hidden="true">
          <circle cx="8" cy="8" r="8" fill="#fff"/>
          <circle cx="8" cy="8" r="4" fill="none" stroke="#141213" stroke-width="1"/>
          <path d="M4 8h8M8 4c-1.6 1.8-1.6 6.2 0 8M8 4c1.6 1.8 1.6 6.2 0 8" fill="none" stroke="#141213" stroke-width="0.9"/>
        </svg>
        <span>www.varqo.com</span>
      </li>
    </ul>

    <div class="person">
      <p class="person__name">Elan Marsh</p>
      <p class="person__role">Managing Director</p>
    </div>
  </section>

  <section class="card card--back" aria-label="Business card back">
    <div class="brand brand--large">
      <span class="brand__dot"></span>
      <span class="brand__name">VARQO</span>
    </div>
    <p class="back__slogan">Your VARQO......</p>
    <p class="back__web">www.varqo.com</p>
  </section>

</body>
</html>
```